IT company needs a wrap design for a Kestra ZLT7

We're a small IT Managed Service Provider (MSP) looking for a 1/2 to 3/4 wrap, not a full.
Car is a 2020 Kestra ZLT7, Blue Flame color. The design should be simple yet creative but not busy or chaotic.

Industry/Entity Type

IT, technology

Requirements
Must have
• company logo, pavlux.example
Should not have
• do not include company phone number

```html
<!DOCTYPE html>
<html lang="en">
<head>
<meta charset="utf-8">
<title>Pavlux vehicle wrap – side panel layout</title>
<link rel="stylesheet" href="https://fonts.googleapis.com/css2?family=Montserrat:wght@500&family=Roboto+Condensed:wght@700&display=swap">
<style>
  :root {
    --stage: #282828;
    --panel: #ffffff;
    --band: #5bc3fe;
    --band-light: #bfe6ff;
    --ink-light: #ffffff;
  }
  html, body {
    margin: 0;
    padding: 0;
    width: 1200px;
    height: 1053px;
    overflow: hidden;
    background: var(--stage);
  }
  .wrap-sheet {
    position: absolute;
    left: 50px;
    top: 366px;
    width: 1100px;
    height: 321px;
    display: block;
  }
  .sheet-base { fill: var(--panel); }
  .brand-band { fill: var(--band); }
  .circuit-field { fill: url(#circuitTone); }
  .brand-mark { fill: var(--ink-light); }
  .brand-name {
    font-family: "Montserrat", sans-serif;
    font-weight: 500;
    font-size: 40px;
    letter-spacing: 22px;
    fill: var(--ink-light);
  }
  .brand-tagline {
    font-family: "Montserrat", sans-serif;
    font-weight: 500;
    font-size: 14px;
    letter-spacing: 5px;
    fill: var(--ink-light);
  }
  .web-address {
    font-family: "Roboto Condensed", sans-serif;
    font-weight: 700;
    font-size: 58px;
    fill: var(--ink-light);
  }
</style>
</head>
<body>
  <svg class="wrap-sheet" viewBox="0 0 1708 499" preserveAspectRatio="none" xmlns="http://www.w3.org/2000/svg">
    <defs>
      <linearGradient id="circuitTone" x1="0" y1="1" x2="1" y2="0">
        <stop offset="0" stop-color="#d6efff"/>
        <stop offset="0.5" stop-color="#a9dcfe"/>
        <stop offset="1" stop-color="#8fd2fe"/>
      </linearGradient>
    </defs>

    <rect class="sheet-base" x="0" y="0" width="1708" height="499"/>

    <polygon class="brand-band" points="243,499 1362,0 1708,0 1708,499"/>

    <polygon class="circuit-field" role="img"
      aria-label="Decorative circuit-style pattern of light blue squares and connector lines on white"
      points="1708,58 1708,499 720,499 900,400 1180,270 1480,150"/>

    <g class="brand-lockup">
      <rect class="brand-mark" x="690" y="318" width="22" height="22" transform="rotate(45 701 329)"/>
      <text class="brand-name" x="585" y="420">PAVLUX</text>
      <text class="brand-tagline" x="818" y="444" text-anchor="end">technology</text>
    </g>

    <text class="web-address" x="885" y="385" transform="rotate(-24 885 385)">pavlux.example</text>
  </svg>
</body>
</html>
```